Web design for boutique law firm

Web design for law firm; practice areas include:
-international intellectual property counseling
-general corporate (contract negotiation, licensing, distribution agreements
-see my *very* outdated website at www.tbkcounsel.com: here is some of the home page content:

"TBK Law Group enjoys providing proactive, business-minded, efficient legal solutions for individuals and companies that benefit from major law firm experience at reasonable rates.

Some areas of emphasis include:

Counseling individuals and companies with respect to clearing, selecting, securing, managing, commercializing, and protecting intellectual property assets around the world. This includes traditional global brand management, marketing, advertising, and enforcement work as well as litigation.
TBK Law Group also provides general counseling services for individuals and businesses, from start-up advice to sophisticated business transactions strategy, agreement negotiating, dispute resolution, and litigation.
Before founding TBK Law Group in 2008, Curtis P. Langford led the Trademark, Copyright, & Brand Management Group for Halbrook & Pemberly's Seattle office. Curtis was also a senior associate at Silicon Valley based Thackery, Olmsted, Vance, & Bellweather."

Target Market(s)

Clients/potential clients needing tier one, international intellectual property advice with "mega" law firm experience for much less than what we were/would be charging at the "mega firms".

Industry/Entity Type

Legal

Number of Pages Required

4 page

Font styles to use
Serif
Sans Serif

Colors

Designer to choose colors to be used in the design.

Requirements
Must have
• +Improvement over everything on current site at www.tbkcounsel.com.
• +Pictures/bios for me and my team (four of us right now).
• +Easy to update and add/remove content.
• +Must be superior in design (look, feel, ease of use, classy and elegant, but hip, reflects international practice).
• +i have logos and color schemes (see current website) but will consider improvements.
Nice to have
• Let me know your thoughts.
Should not have
• No cheese; no overt sales pitches or marketing (since law firm).

```html
<!DOCTYPE html>
<html lang="en">
<head>
<meta charset="utf-8">
<title>TBK Law Group PLLC</title>
<link rel="stylesheet" href="https://fonts.googleapis.com/css2?family=Questrial&family=Roboto+Condensed:wght@400&family=Arimo:wght@400;700&display=swap">
<style>
:root{
  --orange:#f47b20;
  --ink:#1d1d1d;
  --text:#333;
  --muted:#666;
  --black:#0f0f0f;
  --footer:#151515;
  --paper:#ffffff;
  --soft:#f1f0ef;
}
*{box-sizing:border-box;margin:0;padding:0}
html,body{width:1200px;height:3120px;overflow:hidden;background:var(--paper)}
body{position:relative;font-family:"Arimo",Arial,sans-serif;color:var(--text)}
.abs{position:absolute}
.display{font-family:"Questrial","Century Gothic",sans-serif}
.accent{color:var(--orange)}

/* top bar */
.topbar{left:0;top:0;width:1200px;height:31px}
.topbar-phone{left:800px;top:4px;color:#fff;font-size:19px;display:flex;align-items:center;gap:8px}
.topbar-follow{left:965px;top:8px;color:#ddd;font-size:14px;display:flex;align-items:center;gap:10px;padding-left:16px;border-left:1px solid #555}
.dot-social{width:20px;height:20px;border-radius:50%;background:#fff;display:inline-block}

/* header */
.brand{left:112px;top:60px;color:var(--orange);font-size:34px;letter-spacing:1px}
.brand-rule{left:112px;top:112px;width:310px;height:2px;background:var(--orange)}
.nav{left:488px;top:84px;display:flex;gap:28px;font-size:15px;color:var(--ink)}
.nav a{color:inherit;text-decoration:none;padding-top:10px;position:relative}
.nav a.active{color:var(--orange)}
.nav a.active::before{content:"";position:absolute;left:-6px;right:-6px;top:-4px;height:2px;background:var(--orange)}

/* hero */
.hero{left:0;top:131px;width:1200px;height:520px;background:linear-gradient(180deg,#6d7b88 0%,#4a5664 45%,#2f3238 80%,#3a3a3c 100%)}
.hero-arrow{top:373px;width:40px;height:32px;background:#2a2a2a;display:flex;align-items:center;justify-content:center}
.hero-brand{left:108px;top:372px;color:#fff;font-size:36px;letter-spacing:1px}
.hero-tag{left:108px;top:432px;color:#fff;font-family:"Roboto Condensed",sans-serif;font-size:46px}

/* welcome */
.section-title{left:0;width:1200px;text-align:center;font-size:42px;color:var(--ink)}
.title-rule{left:560px;width:80px;height:3px;background:var(--orange)}
.welcome-lead{left:110px;top:760px;width:980px;text-align:center;font-size:13px;font-weight:700;color:var(--ink);line-height:22px}
.welcome-body{left:110px;top:808px;width:980px;text-align:center;font-size:12.5px;color:#444;line-height:22px}
.btn{top:893px;height:38px;display:flex;align-items:center;justify-content:center;font-size:15px;gap:8px}
.btn-dark{left:390px;width:166px;background:var(--black);color:#fff}
.btn-orange{left:552px;width:258px;background:var(--orange);color:#222}

/* services */
.services{left:0;top:984px;width:1200px;height:618px;background:linear-gradient(180deg,#3d2a1f 0%,#6b4a33 40%,#4b3324 70%,#2a1e17 100%)}
.svc-head{color:#fff;font-size:16px;font-weight:700}
.svc-text{color:#eee;font-size:12px;line-height:19px;margin-top:6px}
.svc-left{width:240px;text-align:right}
.svc-right{width:260px;text-align:left}

/* global */
.global-sub{left:80px;top:1740px;width:1040px;text-align:center;font-size:13px;font-weight:700;color:var(--ink)}
.map{left:95px;top:1790px;width:1010px;height:420px;background:radial-gradient(ellipse at 50% 45%,#f3dccd 0%,#f7e8de 55%,#fff 100%)}
.pin{width:16px;height:16px;border-radius:50%;background:var(--orange)}
.map-label{left:740px;top:2003px;font-size:18px;color:#333}

/* people */
.people{left:0;top:2246px;width:1200px;height:500px;background:var(--soft)}
.card{top:2382px;width:229px;height:275px;background:#fff;box-shadow:0 2px 6px rgba(0,0,0,.12);border-bottom:4px solid #222}
.card.featured{border-bottom-color:var(--orange)}
.card-photo{width:229px;height:168px}
.card-name{position:absolute;left:0;top:192px;width:100%;text-align:center;font-size:17px;color:var(--ink)}
.card.featured .card-name{color:var(--orange)}
.card-role{position:absolute;left:0;top:224px;width:100%;text-align:center;font-size:13px;color:#555}
.card-tab{position:absolute;right:0;bottom:-4px;width:48px;height:24px;border-radius:24px 24px 0 0;background:#222;display:flex;align-items:center;justify-content:center}
.card.featured .card-tab{background:var(--orange)}

/* footer */
.footer{left:0;top:2746px;width:1200px;height:322px;background:var(--footer);color:#ddd}
.foot-title{font-size:18px;color:#eee}
.foot-rule{width:44px;height:2px;background:var(--orange);margin-top:10px}
.quick{left:110px;top:2800px}
.quick ul{list-style:none;margin-top:22px}
.quick li{font-size:14px;line-height:32px;color:#ccc}
.quick li::before{content:"› ";color:#888}
.divider{top:2800px;width:1px;height:230px;background:#333}
.contact{left:328px;top:2800px}
.office{top:2848px;font-size:14px;line-height:22px;color:#ddd}
.office-row{display:flex;gap:12px;align-items:flex-start;margin-bottom:18px}
.ic{width:20px;height:20px;border-radius:50%;background:var(--orange);flex:none;margin-top:1px}
.foot-brand{left:890px;top:2870px;display:flex;align-items:center;gap:16px;color:#9a9a9a;font-size:28px}
.foot-circle{width:60px;height:60px;border-radius:50%;border:3px solid #9a9a9a}
.copyright{left:0;top:3068px;width:1200px;height:52px;background:var(--orange);color:#222;font-size:14px;display:flex;align-items:center;justify-content:center}
</style>
</head>
<body>

<!-- top bar -->
<svg class="abs topbar" width="1200" height="31" viewBox="0 0 1200 31"><path d="M580 0H1200V31H612Z" fill="#0f0f0f"/></svg>
<div class="abs topbar-phone">
  <svg width="20" height="20" viewBox="0 0 20 20"><circle cx="10" cy="10" r="10" fill="#f47b20"/><path d="M6.5 5.5l2 2-1 1.2c.7 1.5 1.8 2.6 3.3 3.3l1.2-1 2 2-1.2 1.5C9.5 14.2 5.8 10.5 5 7z" fill="#fff"/></svg>
  555.014.2290
</div>
<div class="abs topbar-follow">Follow Us On <span class="dot-social"></span></div>

<!-- header -->
<div class="abs brand display">TBK LAW GROUP PLLC</div>
<div class="abs brand-rule"></div>
<nav class="abs nav">
  <a class="active">Home</a><a>About Us</a><a>Our Services</a><a>Our Experience</a><a>Our People</a><a>Contact Us</a>
</nav>

<!-- hero -->
<div class="abs hero" role="img" aria-label="Photograph of a businessman silhouetted against city office windows, glasses on a desk in the foreground"></div>
<div class="abs hero-arrow" style="left:0"><svg width="12" height="14"><path d="M9 1L3 7l6 6" stroke="#fff" stroke-width="2" fill="none"/></svg></div>
<div class="abs hero-arrow" style="left:1160px"><svg width="12" height="14"><path d="M3 1l6 6-6 6" stroke="#fff" stroke-width="2" fill="none"/></svg></div>
<div class="abs hero-brand display">TBK LAW GROUP PLLC</div>
<div class="abs hero-tag">Imagine<span class="accent">.</span> Secure<span class="accent">.</span> Protect<span class="accent">.</span></div>

<!-- welcome -->
<h1 class="abs section-title display" style="top:688px;font-weight:400">Welcome To <span class="accent">TBK LAW GROUP PLLC</span></h1>
<div class="abs title-rule" style="top:744px"></div>
<p class="abs welcome-lead">TBK Law Group enjoys providing proactive, business-minded, efficient legal solutions for individuals and companies that benefit from major law firm experience at reasonable rates.</p>
<p class="abs welcome-body">Counseling individuals and companies with respect to clearing, selecting, securing, managing, commercializing, and protecting intellectual property assets around the world. This includes traditional global brand management, marketing, advertising, and enforcement work as well as litigation. TBK Law Group also provides general counseling services for individuals and businesses, from start-up advice to sophisticated business transactions strategy, agreement negotiating, dispute resolution, and litigation.</p>
<div class="abs btn btn-dark">Read More</div>
<div class="abs btn btn-orange">
  <svg width="26" height="18" viewBox="0 0 26 18"><path d="M1 9l6-5 5 3 5-3 8 5-8 6-5-3-5 3z" fill="#3a2a1f"/></svg>
  Request A Free Consultation
</div>

<!-- services -->
<div class="abs services" role="img" aria-label="Photograph of a wood-panelled courtroom interior"></div>
<h2 class="abs section-title display" style="top:1038px;color:#fff;font-weight:400">Our <span class="accent">Services</span></h2>
<div class="abs title-rule" style="top:1094px"></div>

<svg class="abs" style="left:0;top:984px" width="1200" height="618" viewBox="0 984 1200 618">
  <g fill="none" stroke="#fff" stroke-width="1.5">
    <circle cx="600" cy="1320" r="140"/>
    <line x1="460" y1="1200" x2="487" y2="1236"/>
    <line x1="460" y1="1342" x2="460" y2="1332"/>
    <line x1="460" y1="1462" x2="487" y2="1420"/>
    <line x1="740" y1="1200" x2="713" y2="1236"/>
    <line x1="740" y1="1342" x2="740" y2="1332"/>
    <line x1="740" y1="1462" x2="713" y2="1420"/>
  </g>
  <g fill="#fff" stroke="#555">
    <circle cx="487" cy="1236" r="5"/><circle cx="460" cy="1332" r="5"/><circle cx="487" cy="1420" r="5"/>
    <circle cx="713" cy="1236" r="5"/><circle cx="740" cy="1332" r="5"/><circle cx="713" cy="1420" r="5"/>
  </g>
  <circle cx="600" cy="1320" r="98" fill="#fff"/>
  <circle cx="600" cy="1320" r="44" fill="none" stroke="#8a8a8a" stroke-width="3"/>
  <text x="600" y="1395" text-anchor="middle" font-family="Questrial, sans-serif" font-size="17" fill="#8a8a8a">TBK Law Group</text>

  <!-- icon badges -->
  <g stroke="#fff" stroke-width="6">
    <circle cx="415" cy="1200" r="45" fill="#1e1e1e"/>
    <circle cx="415" cy="1342" r="45" fill="#1e1e1e"/>
    <circle cx="415" cy="1468" r="45" fill="#f47b20"/>
    <circle cx="785" cy="1200" r="45" fill="#1e1e1e"/>
    <circle cx="785" cy="1342" r="45" fill="#1e1e1e"/>
    <circle cx="785" cy="1468" r="45" fill="#1e1e1e"/>
  </g>
  <!-- patents: document -->
  <g fill="none" stroke="#fff" stroke-width="2.5">
    <rect x="401" y="1180" width="26" height="36" rx="2"/>
    <line x1="406" y1="1190" x2="422" y2="1190"/><line x1="406" y1="1197" x2="422" y2="1197"/>
    <circle cx="426" cy="1212" r="6"/>
  </g>
  <!-- copyright -->
  <circle cx="415" cy="1342" r="20" fill="none" stroke="#fff" stroke-width="3"/>
  <text x="415" y="1352" text-anchor="middle" font-family="Arimo, sans-serif" font-weight="700" font-size="26" fill="#fff">C</text>
  <!-- registered -->
  <circle cx="415" cy="1468" r="20" fill="none" stroke="#222" stroke-width="3"/>
  <text x="415" y="1478" text-anchor="middle" font-family="Arimo, sans-serif" font-weight="700" font-size="26" fill="#222">R</text>
  <!-- corporate: people -->
  <g fill="#fff">
    <circle cx="785" cy="1190" r="6"/><circle cx="772" cy="1194" r="5"/><circle cx="798" cy="1194" r="5"/>
    <path d="M774 1214a11 11 0 0 1 22 0z"/><path d="M762 1214a9 9 0 0 1 16-4v4z"/><path d="M792 1210a9 9 0 0 1 16 4h-16z"/>
  </g>
  <!-- enforcement: gavel -->
  <g fill="#fff">
    <rect x="770" y="1326" width="26" height="12" rx="2" transform="rotate(-40 783 1332)"/>
    <rect x="783" y="1336" width="6" height="26" transform="rotate(-40 786 1349)"/>
    <rect x="766" y="1360" width="28" height="5"/>
  </g>
  <!-- global: globe -->
  <g fill="none" stroke="#fff" stroke-width="2.5">
    <circle cx="785" cy="1468" r="19"/><ellipse cx="785" cy="1468" rx="8" ry="19"/>
    <line x1="766" y1="1468" x2="804" y2="1468"/><line x1="770" y1="1458" x2="800" y2="1458"/><line x1="770" y1="1478" x2="800" y2="1478"/>
  </g>
</svg>

<div class="abs svc-left" style="left:108px;top:1161px"><div class="svc-head">Patents</div><div class="svc-text">Lorem ipsum dolor sit psum adipiscing sed diam dolor sit mork [+]</div></div>
<div class="abs svc-left" style="left:65px;top:1304px"><div class="svc-head">Copyrights</div><div class="svc-text">Lorem ipsum dolor sit psum adipiscing sed diam dolor sit mork [+]</div></div>
<div class="abs svc-left" style="left:108px;top:1440px"><div class="svc-head">Trademarks</div><div class="svc-text">Lorem ipsum dolor sit psum adipiscing sed diam dolor sit mork [+]</div></div>
<div class="abs svc-right" style="left:852px;top:1165px"><div class="svc-head">Corporate</div><div class="svc-text">Lorem ipsum dolor sit psum adipiscing sed diam dolor sit mork [+]</div></div>
<div class="abs svc-right" style="left:893px;top:1304px"><div class="svc-head">Enforcement / Litigation</div><div class="svc-text">Lorem ipsum dolor sit psum adipiscing sed diam dolor sit mork [+]</div></div>
<div class="abs svc-right" style="left:852px;top:1440px"><div class="svc-head">Global Brand Management</div><div class="svc-text">Lorem ipsum dolor sit psum adipiscing sed diam dolor sit mork [+]</div></div>

<!-- global presence -->
<h2 class="abs section-title display" style="top:1650px;font-weight:400">Global <span class="accent">Presence</span></h2>
<div class="abs title-rule" style="top:1707px"></div>
<p class="abs global-sub">Duis autem vel eum iriure dolor in hendrerit in vulputate velit esse molestie consequat, vel illum dolore eu feugiat nulla facilisis at vero eros et accumsan et iusto</p>
<div class="abs map" role="img" aria-label="Pale peach world map showing office locations"></div>
<div class="abs pin" style="left:250px;top:1856px"></div>
<div class="abs pin" style="left:297px;top:1848px"></div>
<div class="abs pin" style="left:251px;top:1928px"></div>
<div class="abs pin" style="left:285px;top:1938px"></div>
<div class="abs pin" style="left:327px;top:1930px"></div>
<div class="abs pin" style="left:555px;top:1902px"></div>
<div class="abs pin" style="left:581px;top:1882px"></div>
<div class="abs pin" style="left:935px;top:1852px"></div>
<div class="abs pin" style="left:870px;top:1956px"></div>
<div class="abs pin" style="left:900px;top:1968px"></div>
<div class="abs pin" style="left:978px;top:2128px"></div>
<div class="abs" style="left:783px;top:1984px;width:20px;height:20px;border-radius:50%;background:#333"></div>
<div class="abs map-label">Mumbai, India</div>

<!-- our people -->
<div class="abs people"></div>
<h2 class="abs section-title display" style="top:2298px;font-weight:400">Our <span class="accent">People</span></h2>
<div class="abs title-rule" style="top:2355px"></div>

<div class="abs card featured" style="left:106px">
  <div class="card-photo" role="img" aria-label="Portrait photograph of Curtis P. Langford" style="background:linear-gradient(180deg,#d8d8d8,#7a7a7a)"></div>
  <div class="card-name">Curtis P. Langford</div>
  <div class="card-role">Financial Controller</div>
  <div class="card-tab"><svg width="14" height="10"><path d="M2 8l5-5 5 5" stroke="#fff" stroke-width="2" fill="none"/></svg></div>
</div>
<div class="abs card" style="left:366px">
  <div class="card-photo" role="img" aria-label="Portrait photograph of team member" style="background:linear-gradient(180deg,#eef3f6,#c9a58e)"></div>
  <div class="card-name">Marlow Quenby</div>
  <div class="card-role">Designation</div>
  <div class="card-tab"><svg width="14" height="10"><path d="M2 8l5-5 5 5" stroke="#fff" stroke-width="2" fill="none"/></svg></div>
</div>
<div class="abs card" style="left:624px">
  <div class="card-photo" role="img" aria-label="Portrait photograph of team member" style="background:linear-gradient(180deg,#f4eee9,#b57a58)"></div>
  <div class="card-name">Priya Halvorsen</div>
  <div class="card-role">Designation</div>
  <div class="card-tab"><svg width="14" height="10"><path d="M2 8l5-5 5 5" stroke="#fff" stroke-width="2" fill="none"/></svg></div>
</div>
<div class="abs card" style="left:878px">
  <div class="card-photo" role="img" aria-label="Portrait photograph of team member" style="background:linear-gradient(180deg,#f5f3f1,#a8735a)"></div>
  <div class="card-name">Odette Farrance</div>
  <div class="card-role">Designation</div>
  <div class="card-tab"><svg width="14" height="10"><path d="M2 8l5-5 5 5" stroke="#fff" stroke-width="2" fill="none"/></svg></div>
</div>

<!-- footer -->
<div class="abs footer"></div>
<div class="abs quick">
  <div class="foot-title display">Quick Links</div>
  <div class="foot-rule"></div>
  <ul><li>Home</li><li>About Us</li><li>Our Services</li><li>Our Experience</li><li>Our People</li><li>Contact Us</li></ul>
</div>
<div class="abs divider" style="left:308px"></div>
<div class="abs contact">
  <div class="foot-title display">Contact Details</div>
  <div class="foot-rule"></div>
</div>
<div class="abs office" style="left:328px">
  <div class="office-row"><span class="ic"></span><div>Seattle office<br>742 N. Harbor Ave. Suite 4<br>Seattle WA 98100</div></div>
  <div class="office-row"><span class="ic"></span><div>555.014.2290</div></div>
  <div class="office-row"><span class="ic"></span><div>555.014.2291</div></div>
  <div class="office-row"><span class="ic"></span><div>curtis@tbkcounsel.com</div></div>
</div>
<div class="abs office" style="left:575px">
  <div class="office-row"><span class="ic"></span><div>Boise office<br>Street Name, City Name<br>State Zipcode</div></div>
  <div class="office-row"><span class="ic"></span><div>555.014.2290</div></div>
  <div class="office-row"><span class="ic"></span><div>555.014.2291</div></div>
  <div class="office-row"><span class="ic"></span><div>curtis@tbkcounsel.com</div></div>
</div>
<div class="abs divider" style="left:846px"></div>
<div class="abs foot-brand display"><span class="foot-circle"></span>TBK Law Group</div>
<div class="abs copyright">Copyright © 2017 TBK Law Group pllc. All Rights Reserved.</div>

</body>
</html>
```